FUN Construction Open House Invitation

Open House for New Office of LVDP Construction, we have a logo, not sure what other graphics to put on the invitation and make it fun

Main target audience: Residential Building Architects (Custom Homes)
so we want to maybe target it towards that with a sketch of design/house/plans?
Drinks and food at: Mellow Burrito around the corner
LUCKY DOOR PRIZES: zobex, etc (need to be present to win)
Current BORING design attached
Event is on Thursday, 7/15 from 3-6 pm
Location: 518 Kelmont Row, Suite 307-2 in Laguna Beach
Company: LVDP Construction (logo attached)
RSVP by 7/12 to office@lvdp.construction or 949-555-0173

Target Market(s)

Residential Building Architects for Custom Homes

Font styles to use
Other font styles liked:
• SOMETHING MODERN

Requirements
Must have
• Graphics, MODERN & FUN & ARTSY look but not too crowded
Should it be a charicature of the team? (with our english bulldog?)
A charicature of our english bulldog on a surfboard or skateboard or too cheesy?
Should not have
• Hammer or any other graphics like that, we are not a handyman company
High end custom home construction working with architects

```html
<!DOCTYPE html>
<html lang="en">
<head>
<meta charset="utf-8">
<title>LVDP Construction — Open House Invitation</title>
<link rel="stylesheet" href="https://fonts.googleapis.com/css2?family=Exo+2:wght@400;500;600;700;800&family=Michroma&display=swap">
<style>
  :root {
    --orange: #ec7416;
    --black: #050505;
    --ink: #222222;
    --paper: #f6f6f6;
    --mist-a: #dedede;
    --mist-b: #f4f4f4;
    --white: #ffffff;
    --gold-a: #f6d36b;
    --gold-b: #b8860b;
    --stage: #606060;
  }
  * { box-sizing: border-box; margin: 0; padding: 0; }
  html, body { width: 989px; height: 1200px; overflow: hidden; }
  body {
    background: var(--stage);
    font-family: "Exo 2", sans-serif;
    position: relative;
  }
  .invitation {
    position: absolute;
    left: 25px; top: 281px;
    width: 939px; height: 638px;
    background: var(--orange);
    padding: 17px;
    display: flex; flex-direction: column;
  }
  .band { position: relative; width: 100%; }

  .title-band {
    height: 142px;
    background: linear-gradient(110deg, var(--mist-a) 0%, var(--mist-b) 45%, var(--mist-a) 100%);
    text-align: center;
    padding-top: 36px;
  }
  .title-band h1 {
    font-family: "Michroma", sans-serif;
    font-size: 28px; font-weight: 400;
    color: var(--ink);
    letter-spacing: 0.5px;
    -webkit-text-stroke: 0.6px var(--ink);
  }
  .title-band .audience {
    font-family: "Michroma", sans-serif;
    font-size: 28px;
    color: var(--orange);
    -webkit-text-stroke: 0.6px var(--orange);
    margin-top: 6px;
  }

  .event-band {
    height: 215px;
    background: var(--black);
    color: var(--white);
    text-align: center;
  }
  .when {
    display: flex; justify-content: center; align-items: center;
    padding-top: 20px;
  }
  .when > div { padding: 0 24px; }
  .when .day { font-size: 29px; font-weight: 700; letter-spacing: 0.5px; }
  .when .date { font-size: 38px; font-weight: 800; line-height: 1.25; }
  .when .date sup { font-size: 20px; vertical-align: 16px; }
  .when .time { font-size: 29px; font-weight: 700; }
  .divider { width: 0; height: 92px; border-left: 3px dotted var(--orange); padding: 0 !important; }
  .where-label { color: var(--orange); font-size: 27px; font-weight: 700; margin-top: 8px; }
  .where { font-size: 27px; font-weight: 500; margin-top: 2px; }

  .perks-band {
    height: 96px;
    background: var(--paper);
    display: flex; align-items: center;
  }
  .perk { flex: 1; display: flex; align-items: center; padding-left: 42px; }
  .perk + .perk { padding-left: 22px; }
  .perk-icon { width: 40px; height: 50px; background: rgba(236,116,22,0.25); border-radius: 6px; margin-right: 12px; flex: none; }
  .perk-title { color: var(--orange); font-size: 21px; font-weight: 700; }
  .perk-title span { color: var(--ink); font-weight: 500; }
  .perk-text { color: var(--ink); font-size: 21px; font-weight: 500; }
  .perks-divider { width: 0; height: 66px; border-left: 3px dotted var(--orange); }

  .rsvp-band {
    flex: 1;
    background: var(--black);
    color: var(--white);
    display: flex; align-items: center; justify-content: space-between;
    padding: 0 40px 0 45px;
  }
  .rsvp-title { color: var(--orange); font-size: 23px; font-weight: 700; }
  .contact { font-size: 23px; font-weight: 500; display: flex; align-items: center; gap: 8px; margin-top: 3px; }
  .contact .or { color: var(--orange); font-weight: 700; }
  .contact svg { flex: none; }
  .brand { display: flex; align-items: center; gap: 12px; margin-top: 18px; }
  .brand-mark { width: 22px; height: 22px; background: var(--orange); }
  .brand-name { color: var(--orange); font-size: 34px; font-weight: 800; letter-spacing: 1px; }

  .ribbon {
    position: absolute; width: 20px; border-radius: 10px;
    background: linear-gradient(180deg, var(--gold-a), var(--gold-b));
  }
</style>
</head>
<body>
  <main class="invitation">
    <section class="band title-band">
      <div class="ribbon" role="img" aria-label="gold confetti ribbon" style="left:24px;top:55px;height:125px;"></div>
      <div class="ribbon" role="img" aria-label="gold confetti ribbon" style="right:22px;top:40px;height:150px;"></div>
      <h1>RESIDENTIAL BUILDING ARCHITECTS</h1>
      <p class="audience">(CUSTOM HOMES)</p>
    </section>

    <section class="band event-band">
      <div class="ribbon" role="img" aria-label="gold confetti ribbon" style="left:65px;top:55px;height:130px;"></div>
      <div class="ribbon" role="img" aria-label="gold confetti ribbon" style="right:65px;top:75px;height:95px;"></div>
      <div class="when">
        <div class="day">THURSDAY</div>
        <div class="divider"></div>
        <div class="date">JULY 15<sup>TH</sup><br>2021</div>
        <div class="divider"></div>
        <div class="time">3 pm-6 pm</div>
      </div>
      <p class="where-label">LVDP’s new office Location at</p>
      <p class="where">518 Kelmont Row, Suite 307-2 in Laguna Beach</p>
    </section>

    <section class="band perks-band">
      <div class="perk">
        <div class="perk-icon" role="img" aria-label="food and drink icon"></div>
        <div>
          <p class="perk-title">DRINKS AND FOOD AT:</p>
          <p class="perk-text">Mellow Burrito around the corner</p>
        </div>
      </div>
      <div class="perks-divider"></div>
      <div class="perk">
        <div class="perk-icon" role="img" aria-label="prize ticket icon"></div>
        <div>
          <p class="perk-title">LUCKY DOOR PRIZES: <span>zobex, etc</span></p>
          <p class="perk-text">(need to be present to win)</p>
        </div>
      </div>
    </section>

    <section class="band rsvp-band">
      <div class="ribbon" role="img" aria-label="gold confetti ribbon" style="right:22px;top:-30px;height:100px;"></div>
      <div class="rsvp">
        <p class="rsvp-title">RSVP by 7/12 to</p>
        <p class="contact">
          <svg width="22" height="16" viewBox="0 0 22 16"><rect x="1" y="1" width="20" height="14" rx="2" fill="none" stroke="#ec7416" stroke-width="2"/><path d="M1 2 L11 9 L21 2" fill="none" stroke="#ec7416" stroke-width="2"/></svg>
          office@lvdp.construction <span class="or">or</span>
        </p>
        <p class="contact">
          <svg width="20" height="20" viewBox="0 0 20 20"><path d="M4 2 L8 2 L9 6 L7 8 Q9 12 12 13 L14 11 L18 12 L18 16 Q17 18 15 18 Q4 16 2 5 Q2 3 4 2Z" fill="none" stroke="#ec7416" stroke-width="2"/></svg>
          949-555-0173
          <svg width="20" height="20" viewBox="0 0 20 20"><circle cx="10" cy="10" r="8" fill="none" stroke="#ec7416" stroke-width="2"/><ellipse cx="10" cy="10" rx="3.5" ry="8" fill="none" stroke="#ec7416" stroke-width="1.6"/><path d="M2 10 H18" stroke="#ec7416" stroke-width="1.6"/></svg>
          www.lvdp.construction
        </p>
      </div>
      <div class="brand">
        <span class="brand-mark"></span>
        <span class="brand-name">LVDP CONSTRUCTION</span>
      </div>
    </section>
  </main>
</body>
</html>
```